Orvel Prime - Letter Head

My company is a residential and commercial cleaning company , which is located in Abu Dhabi, UAE.
I am looking for a creative letterhead reflects the professional and reflects professionalism and send the feeling of relax and comfort.
The color which will be used it has to be selected carefully in prospective of colors psychological effects, so every color to be used should be for a reason.
Also, reflecting my company colors in an attractive way.
Regarding the information which it should contains, it has to show the address, contacts , telephones an, email address and website.
Also, my company logo is attached
Residential

```html
<!DOCTYPE html>
<html lang="en">
<head>
<meta charset="utf-8">
<title>Orvel Prime – Letterhead</title>
<link rel="stylesheet" href="https://fonts.googleapis.com/css2?family=Lato:wght@400;700&family=Open+Sans:wght@400&display=swap">
<style>
  :root {
    --backdrop: #e4e5e7;
    --paper: #eef0f1;
    --ink: #1f1f1f;
    --brand-blue: #1f6fb8;
    --leaf-light: #a6d84a;
    --leaf-mid: #6cc13a;
    --leaf-deep: #3f9a2a;
    --signature-ink: #8a97c4;
    --watermark: rgba(120, 120, 120, 0.09);
  }
  * { margin: 0; padding: 0; box-sizing: border-box; }
  html, body {
    width: 1113px; height: 1200px; overflow: hidden;
    background: var(--backdrop);
  }
  .letterhead {
    position: absolute; left: 214px; top: 99px;
    width: 716px; height: 1012px;
    background: var(--paper);
    font-family: "Lato", sans-serif;
    color: var(--ink);
    overflow: hidden;
  }
  .brand {
    position: absolute; left: 0; right: 0; top: 52px;
    display: flex; justify-content: center; align-items: center; gap: 12px;
  }
  .brand-name {
    font-family: "Lato", sans-serif; font-weight: 700;
    font-size: 36px; color: var(--brand-blue); letter-spacing: -0.5px;
  }
  .brand-dot {
    width: 30px; height: 30px; border-radius: 50%;
    background: var(--leaf-mid);
  }
  .watermark {
    position: absolute; left: 60px; top: 370px; width: 600px;
    text-align: center;
    font-family: "Lato", sans-serif; font-weight: 700;
    font-size: 110px; line-height: 1; color: var(--watermark);
    white-space: nowrap;
  }
  .greeting {
    position: absolute; left: 83px; top: 212px;
    font-size: 21px; font-weight: 400;
  }
  .letter-body {
    position: absolute; left: 83px; top: 279px; width: 544px;
    font-size: 12.6px; line-height: 19.85px; text-align: justify;
  }
  .letter-body p + p { margin-top: 19.85px; }
  .closing {
    position: absolute; right: 112px; top: 656px;
    font-size: 12.6px;
  }
  .signature {
    position: absolute; left: 455px; top: 686px;
    width: 160px; height: 66px;
    background: linear-gradient(100deg, rgba(138,151,196,0.18), rgba(138,151,196,0.08));
    border-radius: 6px;
  }
  .leaf-art {
    position: absolute; left: 8px; top: 716px;
    width: 356px; height: 296px;
    background: radial-gradient(ellipse at 45% 55%, var(--leaf-mid) 0%, var(--leaf-light) 45%, rgba(166,216,74,0) 72%);
    opacity: 0.85;
  }
  .contact {
    position: absolute; right: 14px; top: 924px;
    font-family: "Open Sans", sans-serif; font-size: 14.5px;
    line-height: 24px; text-align: right; color: var(--ink);
    list-style: none;
  }
</style>
</head>
<body>
  <main class="letterhead">
    <header class="brand">
      <span class="brand-name">Orvel Prime</span>
      <span class="brand-dot" aria-hidden="true"></span>
    </header>

    <div class="watermark" aria-hidden="true">Orvel Prime</div>

    <h1 class="greeting">Dear Mr. Harlow,</h1>

    <section class="letter-body">
      <p>Lorem ipsum dolor sit amet, consectetur adipiscing elit. Donec orci purus, luctus vitae dignissim eu, iaculis sed purus. Vivamus faucibus, ipsum nec aliquet viverra, leo mauris condimentum ligula, sit amet sagittis enim ligula quis arcu. Nam egestas tortor id nisi porttitor mattis. In tortor ante, ultricies in suscipit a, tempus non massa. Vivamus et auctor mi. Fusce vel massa nulla. Phasellus nec eros mauris, et scelerisque orci.</p>
      <p>Donec malesuada orci vitae nulla accumsan porta a id massa. Quisque accumsan iaculis magna sit amet fringilla. Maecenas consequat, magna eget tincidunt semper, odio nibh rutrum mi, id feugiat ante nisi eu risus. Vestibulum nunc orci, rhoncus a placerat in, ultricies in mi. Cras mattis varius eros, vel fringilla nisi suscipit eget. Quisque scelerisque sagittis nulla at porttitor.</p>
      <p>Sed id augue vitae urna euismod commodo aliquet a quam. Pellentesque arcu velit, cursus et malesuada ut, consequat et diam. Nullam erat sem, rhoncus id ullamcorper vitae, rhoncus et arcu. In ultricies ultricies nulla, ut rutrum nisi iaculis at. Donec eu magna a metus ornare faucibus. Fusce aliquet faucibus ultricies. Morbi semper, est id tincidunt gravida, sem arcu adipiscing lacus, ac bibendum nulla leo eu purus. Quisque nec diam sed risus consectetur a ccumsan quis quis nibh. Vestibulum id purus lorem.</p>
    </section>

    <p class="closing">Sincerely,</p>
    <div class="signature" role="img" aria-label="Handwritten signature of the sender"></div>

    <div class="leaf-art" role="img" aria-label="Illustration of a curving green sprig with dewy leaves"></div>

    <ul class="contact">
      <li>Web: orvelprime.ae</li>
      <li>E-mail: hello@orvelprime.ae</li>
      <li>Tel: 555 0142</li>
    </ul>
  </main>
</body>
</html>
```